Begegnungskonzert Kammerchor Lumivessa Berlin und Tonbrückener Kinderchor Peking
Zielgruppe
Es geht um ein Konzertplakat für den Kammerchor Lumivessa Berlin. www.lumivessa-chor.example
Wir haben ein Begegnungskonzert mit einem Chinesischen Kinderchor, der Berlin besucht.
Aufgabenstellung
Kammerchor Lumivessa Berlin, Leitung: Karsten Brodt
Tonbrückener Kinderchor Peking, Leitung: Prof. Zhou Wen
21.08.2017, 19:00 Uhr Quellkapelle Berlin Wilmersdorf, Falkenauer Str. 27, 14183 Berlin
Eintritt frei, Spenden erbeten
Werke von Albrechtsen, Caspo, Thornvik, Pemberley und vielen mehr...
Logos und Farben bitte von unserer Website übernehmen!

```html
<!DOCTYPE html>
<html lang="de">
<head>
<meta charset="utf-8">
<title>Begegnungskonzert Berlin//Peking</title>
<link href="https://fonts.googleapis.com/css2?family=Roboto:wght@400;700&display=swap" rel="stylesheet">
<style>
  :root {
    --ink: #1c1c1c;
    --black: #181818;
    --paper: #ffffff;
    --backdrop: #e9e9e7;
    --photo-warm-a: #8a7258;
    --photo-warm-b: #2a2230;
    --photo-hall-a: #6e5446;
    --photo-hall-b: #1e1a1c;
  }
  * { margin: 0; padding: 0; box-sizing: border-box; }
  html, body { width: 1200px; height: 928px; overflow: hidden; background: var(--backdrop); }
  body { font-family: "Roboto", Arial, sans-serif; color: var(--ink); position: relative; }

  .poster {
    position: absolute; left: 294px; top: 24px;
    width: 574px; height: 826px;
    transform: scale(1.065); transform-origin: top left;
    background: var(--paper); overflow: hidden;
  }
  .poster__shapes { position: absolute; inset: 0; }

  .ensembles { position: absolute; right: 35px; top: 38px; text-align: right; }
  .ensemble + .ensemble { margin-top: 14px; }
  .ensemble__name { font-weight: 700; font-size: 14px; line-height: 16.5px; text-transform: uppercase; }
  .ensemble__lead { font-size: 10.5px; margin-top: 1px; }

  .brand {
    position: absolute; left: 34px; top: 82px;
    display: flex; align-items: center; gap: 6px;
    color: var(--paper); font-weight: 400; font-size: 14px; line-height: 15px;
  }
  .brand__dot { width: 8px; height: 8px; border-radius: 50%; background: var(--paper); }

  .repertoire { position: absolute; left: 35px; top: 355px; }
  .repertoire__intro { font-size: 10.5px; }
  .repertoire__works { font-weight: 700; font-size: 13.5px; line-height: 16.5px; text-transform: uppercase; }

  .title {
    position: absolute; left: 34px; top: 430px;
    font-weight: 700; font-size: 40.5px; line-height: 43.5px; text-transform: uppercase;
  }

  .event { position: absolute; left: 37px; top: 746px; }
  .event__date { font-weight: 700; font-size: 14px; }
  .event__place { font-size: 10.5px; line-height: 15px; color: #333; }
</style>
</head>
<body>
  <main class="poster">
    <svg class="poster__shapes" viewBox="0 0 574 826" width="574" height="826" aria-hidden="false">
      <defs>
        <linearGradient id="choirWarm" x1="0" y1="0" x2="1" y2="1">
          <stop offset="0" stop-color="var(--photo-warm-a)"/>
          <stop offset="1" stop-color="var(--photo-warm-b)"/>
        </linearGradient>
        <linearGradient id="choirHall" x1="0" y1="0" x2="1" y2="1">
          <stop offset="0" stop-color="var(--photo-hall-a)"/>
          <stop offset="1" stop-color="var(--photo-hall-b)"/>
        </linearGradient>
      </defs>
      <polygon role="img" aria-label="Foto: Dirigent vor dem Kinderchor in Uniform"
               points="0,22 574,197 574,450 504,466 0,312" fill="url(#choirWarm)"/>
      <polygon class="wedge-top" points="0,22 240,91 0,170" fill="var(--black)"/>
      <polygon role="img" aria-label="Foto: Kammerchor mit Bläsern und Dirigent in einer Kirche"
               points="0,620 574,494 574,826 0,826" fill="url(#choirHall)"/>
      <polygon class="wedge-mid" points="430,495 574,445 574,552" fill="var(--black)"/>
      <polygon class="veil" points="0,695 330,826 0,826" fill="var(--paper)" opacity="0.75"/>
    </svg>

    <div class="brand">
      <span class="brand__dot"></span>
      <span class="brand__name">Lumivessa<br>Berlin</span>
    </div>

    <section class="ensembles">
      <div class="ensemble">
        <p class="ensemble__name">Kammerchor Lumivessa<br>Berlin</p>
        <p class="ensemble__lead">Leitung: Karsten Brodt</p>
      </div>
      <div class="ensemble">
        <p class="ensemble__name">Tonbrückener Kinderchor<br>Peking</p>
        <p class="ensemble__lead">Leitung: Prof. Zhou Wen</p>
      </div>
    </section>

    <section class="repertoire">
      <p class="repertoire__intro">Werke von</p>
      <p class="repertoire__works">Albrechtsen,<br>Caspo, Thornvik,<br>Pemberley uvm.</p>
    </section>

    <h1 class="title">Begegnungs-<br>konzert<br>Berlin//Peking</h1>

    <section class="event">
      <p class="event__date">21.8.2017 // 19:00</p>
      <p class="event__place">Quellkapelle Berlin-Wilmersdorf<br>Falkenauer Str. 27 // 14183 Berlin</p>
    </section>
  </main>
</body>
</html>
```